New Wordpress Design Project - Australian native plant nursery

I'm Seeking a wordpress website with landing page with contact details and social links, that page will link to another 4 pages. I'm happy to just add in the information once the template is set up (draft text provided on word doc).
Needing pages of information pages for:
- Nursery, what we carry and that we provide garden design services, pictures of plants and gardens
- Native flowers & what we provide, flower arrangements for weddings, special occasions, pictures
- Giftwear short blurb that we carry local artisan giftwear, pictures
- about us with history of the nursery & pictures
* Also wanting a link for e-gift cards. The link will go to an external page (square) so I don’t need to set up the website for purchases.
Social media links
Social links
https://www.facebook.com/TheBrambleHollow
https://www.instagram.com/thebramblehollownursery

Two local native nursery websites that I like the style of:
https://www.harbourfernplantnursery.com.au/
https://www.belmaro.com.au/

I'm using two versions of our logo, we have the smaller circle and then the other logo which is stretched out. We have used the second design for our signs at the nursery, I've asked the sign guy for a copy of the design as I don't currently have one. I have vector files of the other design.

We have wordpress set up with elemantor and hosting with godaddy, I can send you the logon details once design is confirmed.

Target Market(s)

Anyone who likes gardening, we have a pretty even spread of customers across male/female and all ages

Industry/Entity Type

Garden centre with native plants, flowers and giftwear

Coding

Coded - Design and coding required

Colors
0054AA
0677BA
7BADD7
CADEEF
E8F1F8
0094D4
00A9DD
6FCCEA
C7EBF8
E9F6FB
00AB8E
00BBA5
67D7C9
C6EFE9
E9F9F6

Requirements
Must have
• Organic/modern/minimalist design
Nice to have
• Blue/white/green, flannel flowers as per logo

```html
<!DOCTYPE html>
<html lang="en">
<head>
<meta charset="utf-8">
<title>The Bramble Hollow – Australian Plants, Flowers and Giftware</title>
<link href="https://fonts.googleapis.com/css2?family=Poppins:wght@300;400;500;600;700&display=swap" rel="stylesheet">
<style>
:root{
  --navy:#34536f;
  --ink:#222a33;
  --grey-bg:#f1f1f1;
  --white:#ffffff;
  --arrow:#c4c4c4;
  --star:#f2a81d;
}
*{margin:0;padding:0;box-sizing:border-box}
html,body{width:1200px;height:4498px;overflow:hidden}
body{font-family:'Poppins',sans-serif;color:var(--ink);background:var(--white);position:relative}
a{color:inherit;text-decoration:none}
.abs{position:absolute}

/* header */
.site-header{position:absolute;left:0;top:0;width:1200px;height:129px;background:var(--white)}
.brand{position:absolute;left:92px;top:22px;display:flex;align-items:center;gap:12px}
.brand-mark{width:60px;height:60px;border:2px solid var(--navy);border-radius:50%}
.brand-name{font-size:26px;font-weight:400;color:var(--navy);line-height:1.1}
.brand-tag{position:absolute;left:92px;top:100px;font-size:9px;color:var(--navy);letter-spacing:.3px}
.main-nav{position:absolute;top:56px;left:0;width:1200px;font-size:15px;color:var(--ink)}
.main-nav a{position:absolute}

/* hero */
.hero{position:absolute;left:0;top:129px;width:1200px;height:545px;overflow:hidden}
.hero-photo{position:absolute;inset:0;background:radial-gradient(circle at 78% 30%,#f6f3e6 0,#e9e2c4 14%,#8e9a52 32%,#4e6530 55%,#33461f 80%)}
.hero h1{position:absolute;left:86px;top:196px;font-size:46px;font-weight:700;color:var(--white);letter-spacing:.5px}
.hero p{position:absolute;left:86px;top:266px;font-size:15px;line-height:23px;color:var(--white)}
.btn-ghost{position:absolute;width:285px;height:66px;border:2px solid var(--white);border-radius:33px;color:var(--white);font-size:19px;display:flex;align-items:center;justify-content:center}
.hero .btn-ghost{left:86px;top:350px}
.hero-wave{position:absolute;left:0;bottom:0;width:1200px;height:70px}

/* headings */
.sec-title{position:absolute;color:var(--navy)}
.sec-title .kicker{display:block;font-size:25px;font-weight:400}
.sec-title .main{display:block;font-size:44px;font-weight:500;line-height:1.05}
.rule{position:absolute;height:3px;background:var(--navy);width:110px}

/* nursery */
.cloud{position:absolute;width:320px;height:262px;clip-path:url(#cloud)}
.caption{position:absolute;width:320px;text-align:center;font-size:15px;line-height:24px;color:var(--ink)}

/* native flowers */
.band-grey{position:absolute;left:0;width:1200px;background:var(--grey-bg)}
.sub-head{position:absolute;left:87px;font-size:26px;font-weight:400;color:var(--ink)}
.frame{position:absolute;width:326px;height:241px;background:var(--white);border-radius:14px;padding:14px}
.frame div{width:100%;height:100%;border-radius:8px}

/* giftwear */
.band-navy{position:absolute;left:0;top:2309px;width:1200px;height:547px;background:var(--navy)}
.band-navy .sec-title .main{color:var(--white)}
.gift-photo{position:absolute;width:318px;height:219px;border-radius:48px}
.gift-cap{position:absolute;width:340px;text-align:center;font-size:15px;line-height:24px;color:var(--white)}

/* justified fixed lines */
.jline{display:block;text-align:justify;text-align-last:justify;white-space:nowrap}
.jline.end{text-align-last:left}

/* about */
.about-copy{position:absolute;left:87px;top:3181px;width:408px;font-size:15.5px;line-height:31px;color:var(--ink)}
.btn-outline{position:absolute;width:285px;height:66px;border:2px solid var(--navy);border-radius:33px;color:var(--navy);font-size:19px;display:flex;align-items:center;justify-content:center}
.about-ring{position:absolute;left:560px;top:3006px;width:504px;height:504px;border-radius:50%;border:5px solid #4d4d4d;border-left-color:transparent;border-top-color:transparent;transform:rotate(10deg)}
.about-photo{position:absolute;left:576px;top:3022px;width:472px;height:472px;border-radius:50%;background:radial-gradient(circle at 45% 45%,#6f9b3f 0,#4d7a2b 30%,#5a4330 62%,#3a2c22 100%)}

/* testimonials */
.quote-card{position:absolute;top:3815px;width:422px;height:272px;background:var(--white);border-radius:8px;box-shadow:0 2px 10px rgba(0,0,0,.08)}
.quote-badge{position:absolute;top:-20px;left:50%;margin-left:-21px;width:42px;height:42px;border-radius:50%;background:var(--navy);color:var(--white);font-size:34px;font-weight:700;line-height:56px;text-align:center}
.quote-text{position:absolute;left:42px;top:60px;width:336px;font-size:14.5px;line-height:21px;color:var(--ink)}
.avatar{position:absolute;left:44px;top:158px;width:77px;height:77px;border-radius:50%;background:linear-gradient(#c9ced4,#7e8792)}
.role{position:absolute;left:142px;top:184px;font-size:9px;color:#555}
.stars{position:absolute;left:142px;top:201px;font-size:12px;color:var(--star);letter-spacing:1px;line-height:14px}
.slider-arrow{position:absolute;top:3918px;width:38px;height:38px;border-radius:50%;background:var(--arrow)}
.slider-arrow svg{position:absolute;left:11px;top:11px}

/* footer */
.site-footer{position:absolute;left:0;top:4120px;width:1200px;height:378px}
.site-footer .fill{position:absolute;left:0;top:50px;width:1200px;height:328px;background:var(--navy)}
.foot-nav{position:absolute;top:145px;left:0;width:1200px;font-size:16px;color:var(--white)}
.foot-nav a{position:absolute}
.dash{position:absolute;left:80px;width:1030px;border-top:1px dashed #7e95ab}
.contact{position:absolute;top:222px;color:var(--white);font-size:15px;line-height:19px}
.contact .label{font-weight:600;font-size:14px;margin-bottom:6px}
.contact-icon{position:absolute;top:210px;width:38px;height:38px;border-radius:50%;background:var(--white)}
.contact-icon svg{position:absolute;left:9px;top:9px}
.copyright{position:absolute;left:85px;top:326px;font-size:15px;color:var(--white)}
.social{position:absolute;top:315px;width:38px;height:38px;border-radius:50%;border:2px solid var(--white)}
</style>
</head>
<body>

<svg width="0" height="0" style="position:absolute">
  <defs>
    <clipPath id="cloud" clipPathUnits="objectBoundingBox">
      <circle cx=".5" cy=".5" r=".34"/>
      <circle cx=".5" cy=".18" r=".18"/>
      <circle cx=".22" cy=".3" r=".18"/>
      <circle cx=".78" cy=".3" r=".18"/>
      <circle cx=".15" cy=".58" r=".17"/>
      <circle cx=".85" cy=".58" r=".17"/>
      <circle cx=".3" cy=".8" r=".18"/>
      <circle cx=".7" cy=".8" r=".18"/>
      <circle cx=".5" cy=".84" r=".16"/>
    </clipPath>
  </defs>
</svg>

<header class="site-header">
  <a class="brand" href="#">
    <span class="brand-mark"></span>
    <span class="brand-name">The Bramble Hollow</span>
  </a>
  <span class="brand-tag">Australian Plants • Flowers and Giftware</span>
  <nav class="main-nav">
    <a href="#" style="left:443px">Home</a>
    <a href="#" style="left:535px">About Us</a>
    <a href="#" style="left:658px">Nursery</a>
    <a href="#" style="left:751px">Native Flowers</a>
    <a href="#" style="left:905px">Gift Wear</a>
    <a href="#" style="left:1028px">Contact Us</a>
  </nav>
</header>

<section class="hero">
  <div class="hero-photo" role="img" aria-label="Close-up of a white daisy with a yellow centre in a blurred green meadow"></div>
  <h1>IPSUM DOLOR SIT AME</h1>
  <p>Lorem ipsum dolor sit amet, consectetur adipiscing elit,<br>sed do eiusmod tempor &nbsp;ncididunt ut labore et dolore</p>
  <a class="btn-ghost" href="#">Book Now</a>
  <svg class="hero-wave" viewBox="0 0 1200 70" preserveAspectRatio="none">
    <path d="M0 70 C120 70 180 0 330 10 C470 20 520 60 640 45 C760 30 820 0 960 10 C1080 18 1140 60 1200 70 Z" fill="#fff"/>
  </svg>
</section>

<section class="nursery">
  <h2 class="sec-title" style="left:346px;top:744px"><span class="kicker">Nursery &amp;</span><span class="main">Garden Design Services</span></h2>
  <span class="rule" style="left:356px;top:836px"></span>

  <div class="cloud" style="left:82px;top:908px;background:linear-gradient(#5f7d3a,#2f4a22)" role="img" aria-label="Rows of potted green shrubs in a nursery"></div>
  <div class="cloud" style="left:442px;top:908px;background:linear-gradient(#7f9a2e,#c9c22a)" role="img" aria-label="Gardener tending yellow flowering plants"></div>
  <div class="cloud" style="left:798px;top:908px;background:linear-gradient(#b9d3e6,#c86a7a 60%,#5d7b3a)" role="img" aria-label="Shoppers among colourful flowers in a garden centre"></div>

  <p class="caption" style="left:82px;top:1183px">Lorem ipsum dolor sit amet, conse<br>fghctetur adipiscing elit, sed do eiu<br>smod tempor incididunt ut labore et</p>
  <p class="caption" style="left:442px;top:1183px">Lorem ipsum dolor sit amet, conse<br>fghctetur adipiscing elit, sed do eiu<br>smod tempor incididunt ut labore et</p>
  <p class="caption" style="left:814px;top:1183px">Lorem ipsum dolor sit amet, conse<br>fghctetur adipiscing elit, sed do eiu<br>smod tempor incididunt ut labore et</p>
</section>

<section class="band-grey" style="top:1301px;height:1008px">
  <h2 class="sec-title" style="left:421px;top:89px"><span class="kicker">Native flowers &amp;</span><span class="main">What We Provide</span></h2>
  <span class="rule" style="left:431px;top:182px"></span>

  <h3 class="sub-head" style="top:236px">Flower arrangements for weddings</h3>
  <div class="frame" style="left:79px;top:302px"><div style="background:linear-gradient(135deg,#b84e7a,#d6dbe2 70%)" role="img" aria-label="Pink wedding bouquet against a pale sky"></div></div>
  <div class="frame" style="left:437px;top:302px"><div style="background:linear-gradient(90deg,#d9d9d9 30%,#7b63b8)" role="img" aria-label="Purple flower bouquet on white fabric"></div></div>
  <div class="frame" style="left:798px;top:302px"><div style="background:linear-gradient(#3e6a36,#e7d6c0 60%,#c9ad82)" role="img" aria-label="Wedding aisle lined with floral arrangements"></div></div>

  <h3 class="sub-head" style="top:615px">Flower arrangements for special occasions</h3>
  <div class="frame" style="left:79px;top:676px"><div style="background:linear-gradient(135deg,#3c4a45,#f0a070 50%,#e9b49a)" role="img" aria-label="Peach roses and orange poppies"></div></div>
  <div class="frame" style="left:437px;top:676px"><div style="background:linear-gradient(#c7352f,#3f6b32 60%,#8b7a66)" role="img" aria-label="Market stall of red and pink flowers"></div></div>
  <div class="frame" style="left:798px;top:676px"><div style="background:linear-gradient(135deg,#9a90e0,#c9304a 50%,#e6a4bd)" role="img" aria-label="Red roses in a white gift bag"></div></div>
</section>

<section class="band-navy">
  <h2 class="sec-title" style="left:509px;top:70px"><span class="main">Giftwear</span></h2>
  <span class="rule" style="left:509px;top:141px;background:#fff;width:104px"></span>

  <div class="gift-photo" style="left:82px;top:197px;background:linear-gradient(135deg,#a35a45,#dcdcdc 45%,#c9c9c9)" role="img" aria-label="Hands holding a silver gift box with orange ribbon"></div>
  <div class="gift-photo" style="left:441px;top:197px;background:linear-gradient(#b31b22,#d07a43 50%,#b31b22)" role="img" aria-label="Hands holding a patterned gift box"></div>
  <div class="gift-photo" style="left:800px;top:197px;background:linear-gradient(135deg,#2d3a5a,#ef6a2c 50%,#e8b730)" role="img" aria-label="Stacked orange gift boxes with marigolds"></div>

  <p class="gift-cap" style="left:71px;top:448px">Lorem ipsum dolor sit amet, consec<br>tetur adipiscing elit, sed do eiugfjj</p>
  <p class="gift-cap" style="left:430px;top:448px">Lorem ipsum dolor sit amet, consec<br>tetur adipiscing elit, sed do eiugfjj</p>
  <p class="gift-cap" style="left:795px;top:448px">Lorem ipsum dolor sit amet, consec<br>tetur adipiscing elit, sed do eiugfjj</p>
</section>

<section class="about">
  <h2 class="sec-title" style="left:90px;top:3022px"><span class="main">About Us</span></h2>
  <span class="rule" style="left:87px;top:3111px;width:118px"></span>
  <p class="about-copy">
    <span class="jline">Lorem ipsum dolor sit amet, consectetur adipiscing</span>
    <span class="jline">elit, sed do eiusmod tempor incididunt ut labore et</span>
    <span class="jline">dolore magna aliqua. Ut enim ad minim veniam, quis</span>
    <span class="jline">nostrud exercitation ullamco laboris nisi ut aliquip ex</span>
    <span class="jline">ea commodo consequat. Duis aute irure dolor in rep-</span>
    <span class="jline">rehenderit in voluptate velit esse cillum dolore eu</span>
    <span class="jline">fugiat nulla pariatur. Excepteur sint occaecat cupi-</span>
  </p>
  <a class="btn-outline" href="#" style="left:82px;top:3453px">Read More</a>
  <div class="about-ring"></div>
  <div class="about-photo" role="img" aria-label="Fingers holding a young seedling in dark soil"></div>
</section>

<section class="band-grey" style="top:3621px;height:560px">
  <h2 class="sec-title" style="left:444px;top:78px"><span class="main">Happy Clients</span></h2>
</section>
<span class="slider-arrow" style="left:77px"><svg width="16" height="16" viewBox="0 0 16 16"><path d="M10 3 L5 8 L10 13" fill="none" stroke="#fff" stroke-width="2"/></svg></span>
<span class="slider-arrow" style="left:1083px"><svg width="16" height="16" viewBox="0 0 16 16"><path d="M6 3 L11 8 L6 13" fill="none" stroke="#fff" stroke-width="2"/></svg></span>
<article class="quote-card" style="left:160px">
  <span class="quote-badge">”</span>
  <p class="quote-text">
    <span class="jline">Lorem ipsum dolor sit amet, conse ctetur</span>
    <span class="jline">adipiscing elit, sed do eiusmod tempor</span>
    <span class="jline">incididunt ut labore et dolo.” magna ut</span>
    <span class="jline end">labore et dolore magna tempor incididunt ut</span>
  </p>
  <span class="avatar" role="img" aria-label="Client portrait"></span>
  <span class="role">CMO, International</span>
  <span class="stars">★★★★★</span>
</article>
<article class="quote-card" style="left:618px">
  <span class="quote-badge">”</span>
  <p class="quote-text">
    <span class="jline">Lorem ipsum dolor sit amet, conse ctetur</span>
    <span class="jline">adipiscing elit, sed do eiusmod tempor</span>
    <span class="jline">incididunt ut labore et dolo.” magna ut</span>
    <span class="jline end">labore et dolore magna tempor incididunt ut</span>
  </p>
  <span class="avatar" role="img" aria-label="Client portrait"></span>
  <span class="role">CMO, International</span>
  <span class="stars">★★★★★</span>
</article>

<footer class="site-footer">
  <svg class="abs" style="left:0;top:0" width="1200" height="60" viewBox="0 0 1200 60" preserveAspectRatio="none">
    <path d="M0 40 C80 40 120 5 200 10 C300 18 360 45 480 38 C600 30 640 0 760 8 C860 15 900 45 1000 40 C1080 36 1130 10 1200 20 L1200 60 L0 60 Z" fill="#34536f"/>
  </svg>
  <div class="fill"></div>
  <nav class="foot-nav">
    <a href="#" style="left:232px">Home</a>
    <a href="#" style="left:337px">About Us</a>
    <a href="#" style="left:467px">Nursery</a>
    <a href="#" style="left:569px">Native Flowers</a>
    <a href="#" style="left:737px">Gift Wear</a>
    <a href="#" style="left:872px">Contact Us</a>
  </nav>
  <span class="dash" style="top:177px"></span>

  <span class="contact-icon" style="left:213px"><svg width="20" height="20" viewBox="0 0 20 20"><path d="M10 1 C6 1 3.5 4 3.5 7.5 C3.5 12 10 19 10 19 C10 19 16.5 12 16.5 7.5 C16.5 4 14 1 10 1 Z" fill="#34536f"/><circle cx="10" cy="7.5" r="2.5" fill="#fff"/></svg></span>
  <div class="contact" style="left:262px"><div class="label">LOCATION</div>Location Name Dummy<br>address here Pin: 123456</div>
  <span class="contact-icon" style="left:538px"><svg width="20" height="20" viewBox="0 0 20 20"><path d="M5 2 L8 2 L9 6 L7 8 C8 11 9 12 12 13 L14 11 L18 12 L18 15 C18 17 16 18 14 18 C8 17 3 12 2 6 C2 4 3 2 5 2 Z" fill="#34536f"/></svg></span>
  <div class="contact" style="left:588px"><div class="label">CALL US</div>+44 161 555 0148<br>+44 161 555 0193</div>
  <span class="contact-icon" style="left:847px"><svg width="20" height="20" viewBox="0 0 20 20"><rect x="2" y="4" width="16" height="12" rx="1.5" fill="#34536f"/><path d="M2.5 5 L10 11 L17.5 5" fill="none" stroke="#fff" stroke-width="1.5"/></svg></span>
  <div class="contact" style="left:896px"><div class="label">EMAIL</div>xxxxx@bramblehollow.com.au</div>

  <span class="dash" style="top:299px"></span>
  <p class="copyright">Copyright @ 2023 All rights reserved</p>
  <a class="social" href="#" aria-label="Social profile" style="left:1020px"></a>
  <a class="social" href="#" aria-label="Social profile" style="left:1071px"></a>
</footer>

</body>
</html>
```